Marlin Freightways needs Bussiness cards!

Our new trucking company needs business cards!
We need the same design with two different names and emails, everything else it's the same.
I have included our original logo so we can use it for the design.
Note: the logo to be used is the o e with the buffalo on the right side, next to the letters B and E.

Target Market(s)

Trucking, refrigerated transportation, freight

Industry/Entity Type

Business

Contact Information for Business Card

Card #1:
Tomas Ruvalo
tomasruvalo@marlinfreightways.net
1-844-555-0193
(956)555-0172
3817 W. Alder Ave.
Brightwater, KS 78590
www.marlinfreightways.net

Card#2:
Mirabel Quintana
mirabel@marlinfreightways.net
1-844-555-0193
(956)555-0172
3817 W. Alder Ave.
Brightwater, KS 78590
www.marlinfreightways.net

Font styles to use
Sans Serif

Colors
0655a3
ec1f27
ffffff

Requirements
Must have
• our logo
Nice to have
• roads on background,

```html
<!DOCTYPE html>
<html lang="en">
<head>
<meta charset="utf-8">
<title>Marlin Freightways – Business Cards</title>
<link href="https://fonts.googleapis.com/css2?family=Arimo:wght@400;700&display=swap" rel="stylesheet">
<style>
  :root {
    --navy: #0c3a70;
    --navy-deep: #08294f;
    --red: #ec1f27;
    --white: #ffffff;
    --stage: #2a2a2c;
  }
  * { box-sizing: border-box; margin: 0; padding: 0; }
  html, body {
    width: 1200px; height: 950px; overflow: hidden;
    background: var(--stage);
    font-family: "Arimo", Arial, sans-serif;
  }
  .stage { position: relative; width: 1200px; height: 950px; }
  .card {
    position: absolute;
    width: 560px; height: 320px;
    overflow: hidden;
    box-shadow: 0 18px 40px rgba(0,0,0,.45);
  }
  /* Front */
  .card-front {
    left: 110px; top: 120px;
    background: linear-gradient(135deg, var(--navy) 0%, var(--navy-deep) 100%);
    color: var(--white);
  }
  .brand {
    display: flex; align-items: center; gap: 12px;
    font-weight: 700; white-space: nowrap;
  }
  .brand-dot { width: 22px; height: 22px; border-radius: 50%; flex: none; }
  .card-front .brand {
    position: absolute; left: 0; right: 0; top: 108px;
    justify-content: center;
    font-size: 36px; color: var(--white);
  }
  .card-front .brand-dot { background: var(--white); }
  .front-web {
    position: absolute; left: 0; right: 0; top: 236px;
    text-align: center; font-size: 13px; letter-spacing: 4px;
    color: var(--white);
  }
  /* Back */
  .card-back {
    left: 530px; top: 500px;
    background: var(--white);
  }
  .back-edge {
    position: absolute; left: 0; top: 0; bottom: 0; width: 12px;
    background: var(--red);
  }
  .card-back .brand {
    position: absolute; left: 36px; top: 176px;
    font-size: 20px; color: var(--navy); gap: 8px;
  }
  .card-back .brand-dot { width: 16px; height: 16px; background: var(--red); }
  .back-panel { position: absolute; left: 0; top: 0; width: 560px; height: 320px; }
  .contact {
    position: absolute; left: 296px; top: 44px; right: 20px;
    color: var(--white);
  }
  .contact-name { font-size: 20px; font-weight: 700; margin-bottom: 28px; }
  .contact-block { font-size: 12.5px; line-height: 1.45; }
  .contact-block + .contact-block { margin-top: 16px; }
</style>
</head>
<body>
<main class="stage">

  <section class="card card-front" aria-label="Business card front">
    <div class="brand"><span class="brand-dot"></span>Marlin Freightways</div>
    <p class="front-web">www.marlinfreightways.net</p>
  </section>

  <section class="card card-back" aria-label="Business card back">
    <div class="back-edge"></div>
    <div class="brand"><span class="brand-dot"></span>Marlin Freightways</div>
    <svg class="back-panel" viewBox="0 0 560 320" aria-hidden="true">
      <polygon points="268,0 560,0 560,320 268,320 268,60 254,48 268,36"
               fill="none" stroke="var(--red)" stroke-width="3"/>
      <polygon points="274,0 560,0 560,320 274,320 274,62 260,48 274,34" fill="var(--navy)"/>
    </svg>
    <div class="contact">
      <p class="contact-name">Tomas Ruvalo</p>
      <p class="contact-block">3817 W. Alder Ave.<br>Brightwater, KS 78590</p>
      <p class="contact-block">
        Phone : 1-844-555-0193<br>
        Mobile : (956)555-0172<br>
        tomasruvalo@marlinfreightways.net<br>
        www.marlinfreightways.net
      </p>
    </div>
  </section>

</main>
</body>
</html>
```